New look while maintaining the Brand identification!

I want a new look for my business card. I want to keep the same colors and feel but change the look and layout a bit. The logo (KALMORETIX Physical therapy Reimagined and the lilypad) must remain the same and in that font.
We are a physical therapy clinic. So we have certification that we can write on the back or services we provide (which is what we currently have on the back of the card as well)

Contact information
2840 Cedar Hollow Rd., #22
Naples, FL 34276
P: (239) 555-0172
F: (239) 555-0198
E: kalmoretixcare@mailvexo.com
W: www.kalmoretixcare-example.com

Industry/Entity Type

Physical Therapy

Contact Information for Business Card

Our current cards have the business address and information on the back. But I am willing to have it be in the front.

Font styles to use
Sans Serif

Colors
abd036
fbf289
ec1f27

Requirements
Must have
• Has to be unique!
• Services we provide and/or techniques we do must fit on the card
Nice to have
• Would like to have the front and back somehow linked together. Such that if you set the front next to the back, there is a nice flow of design! Currently the back is white with writing on it.
Should not have
• I like the wave lines as compared to straight lines.

```html
<!DOCTYPE html>
<html lang="en">
<head>
<meta charset="utf-8">
<title>Kalmoretix Business Card</title>
<link rel="stylesheet" href="https://fonts.googleapis.com/css2?family=Great+Vibes&family=EB+Garamond:wght@400;500&family=Oswald:wght@700&display=swap">
<style>
  :root {
    --page: #eeeae3;
    --card: #fdfdf8;
    --wash-light: #fbf6cf;
    --wash-deep: #f3ea9e;
    --wave-line: #e3d3a6;
    --leaf-green: #7b9a22;
    --gold: #c9a31d;
    --brand-gold: #c4ac1e;
  }
  * { margin: 0; padding: 0; box-sizing: border-box; }
  html, body { width: 1200px; height: 725px; overflow: hidden; }
  body { background: var(--page); position: relative; font-family: "EB Garamond", Georgia, serif; }

  .card {
    position: absolute;
    width: 540px;
    height: 310px;
    top: 208px;
    background: var(--card);
    box-shadow: 0 6px 18px rgba(90, 70, 40, 0.18);
    overflow: hidden;
  }
  .card--front { left: 40px; }
  .card--back { left: 620px; }
  .card__wave { position: absolute; inset: 0; }

  .flower-photo {
    position: absolute;
    left: 62px; top: 92px;
    width: 130px; height: 118px;
    border-radius: 50%;
    background: radial-gradient(circle at 50% 48%, #f6b21b 0 14%, #fde7a3 24%, #ffffff 48%, #f4f1e8 70%, rgba(253,253,248,0) 72%);
  }

  .holder { position: absolute; right: 20px; top: 52px; text-align: right; }
  .holder__name {
    font-family: "Great Vibes", cursive;
    font-size: 44px; line-height: 1;
    color: var(--leaf-green);
  }
  .holder__degrees { font-size: 19px; color: var(--leaf-green); margin-top: 2px; letter-spacing: 0.3px; }
  .holder__certs { font-size: 11.5px; color: var(--gold); line-height: 1.35; margin-top: 8px; }

  .contact { position: absolute; font-size: 13px; line-height: 1.35; color: var(--gold); }
  .contact--web { right: 20px; top: 196px; text-align: right; }
  .contact--phone { left: 222px; top: 238px; }
  .contact--address { left: 20px; top: 262px; }

  .tagline {
    position: absolute; right: 24px; top: 64px;
    font-family: "Great Vibes", cursive;
    font-size: 34px; color: var(--leaf-green);
  }
  .brand-name {
    position: absolute; right: 26px; bottom: 30px;
    font-family: "Oswald", sans-serif; font-weight: 700;
    font-size: 62px; letter-spacing: 2px; line-height: 1;
    color: var(--brand-gold);
  }
</style>
</head>
<body>

  <section class="card card--front" aria-label="Business card front">
    <svg class="card__wave" width="540" height="310" viewBox="0 0 540 310" aria-hidden="true">
      <defs>
        <linearGradient id="frontWash" x1="0" y1="0" x2="1" y2="0.4">
          <stop offset="0" stop-color="var(--wash-deep)"/>
          <stop offset="0.6" stop-color="var(--wash-light)"/>
          <stop offset="1" stop-color="#fbf8e6"/>
        </linearGradient>
      </defs>
      <path d="M0,0 H540 V48 C360,58 200,110 0,158 Z" fill="url(#frontWash)"/>
      <path d="M540,48 C360,58 200,110 0,158" fill="none" stroke="var(--wave-line)" stroke-width="3"/>
    </svg>

    <div class="flower-photo" role="img" aria-label="Photo of a white water lily with a golden centre"></div>

    <div class="holder">
      <p class="holder__name">Dana Merrowfield,</p>
      <p class="holder__degrees">PT, DTP, MSPT, MBA</p>
      <p class="holder__certs">Certified Lenwick Scoliosis Therapist,<br>Certified Equine Rehab Specialist, CAPP-OB</p>
    </div>

    <p class="contact contact--web">kalmoretixcare@mailvexo.com<br>www.kalmoretixcare-example.com</p>
    <p class="contact contact--phone">P: (239) 555-0172<br>F: (239) 555-0198</p>
    <p class="contact contact--address">2840 Cedar Hollow Rd., #22<br>Naples, FL 34276</p>
  </section>

  <section class="card card--back" aria-label="Business card back">
    <svg class="card__wave" width="540" height="310" viewBox="0 0 540 310" aria-hidden="true">
      <defs>
        <linearGradient id="backWash" x1="0" y1="0" x2="1" y2="0.3">
          <stop offset="0" stop-color="#fbf8e6"/>
          <stop offset="0.5" stop-color="var(--wash-light)"/>
          <stop offset="1" stop-color="var(--wash-deep)"/>
        </linearGradient>
      </defs>
      <path d="M0,0 H540 V140 C420,170 300,110 170,130 C90,142 40,160 0,150 Z" fill="url(#backWash)"/>
      <path d="M540,140 C420,170 300,110 170,130 C90,142 40,160 0,150" fill="none" stroke="var(--wave-line)" stroke-width="3"/>
    </svg>

    <p class="tagline">Physical therapy Reimagined</p>
    <p class="brand-name">KALMORETIX</p>
  </section>

</body>
</html>
```